Pinegate Mobile Imaging
Mobile ultrasound business cards
Danelle Forbush RCS, RDCS(R)
Owner
418 Whitford Ave. Ste 203-117 Marrow Falls, KY 40877
leave space to add later
danelle.forbush@mailbright.net
There is also a second owner that once design is finalized we will need to edit the text to put her information on the card.
email used on card will need to be changed at a later date!

```html
<!DOCTYPE html>
<html lang="en">
<head>
<meta charset="utf-8">
<title>Pinegate Mobile Imaging – Business Card</title>
<link href="https://fonts.googleapis.com/css2?family=Cinzel:wght@400&display=swap" rel="stylesheet">
<style>
  :root {
    --page-bg: #ece9e6;
    --card-white: #ffffff;
    --brand-purple: #7b2f8e;
    --brand-purple-deep: #5e1f70;
    --brand-purple-light: #a05ab2;
    --swoosh-grey: #8a8a8d;
    --swoosh-grey-light: #c9c9cc;
    --text-grey: #6d6d70;
  }
  * { margin: 0; padding: 0; box-sizing: border-box; }
  html, body {
    width: 1200px;
    height: 914px;
    overflow: hidden;
    background: var(--page-bg);
  }
  .canvas {
    position: relative;
    width: 1200px;
    height: 914px;
  }
  .business-card {
    position: absolute;
    left: 60px;
    top: 148px;
    width: 1080px;
    height: 617px;
    background: var(--card-white);
    overflow: hidden;
    box-shadow: 0 6px 24px rgba(0,0,0,0.12);
    font-family: "Cinzel", "Times New Roman", serif;
    font-variant: small-caps;
  }
  .card-swoosh {
    position: absolute;
    inset: 0;
    width: 1080px;
    height: 617px;
  }
  .brand {
    position: absolute;
    left: 70px;
    top: 62px;
    display: flex;
    align-items: center;
    gap: 18px;
  }
  .brand-dot {
    width: 64px;
    height: 64px;
    border-radius: 50%;
    background: var(--brand-purple);
  }
  .brand-name {
    font-size: 34px;
    font-weight: 400;
    color: var(--brand-purple);
    letter-spacing: 0.5px;
  }
  .contact-list {
    position: absolute;
    left: 70px;
    top: 262px;
    list-style: none;
  }
  .contact-item {
    display: flex;
    align-items: center;
    gap: 12px;
    height: 34px;
    font-size: 21px;
    color: var(--brand-purple);
  }
  .contact-item.continuation { padding-left: 36px; }
  .contact-icon {
    width: 24px;
    height: 24px;
    flex: none;
  }
  .owner-block {
    position: absolute;
    right: 62px;
    bottom: 58px;
    text-align: right;
  }
  .owner-name {
    font-size: 23px;
    color: var(--brand-purple);
    letter-spacing: 0.5px;
  }
  .owner-title {
    font-size: 15px;
    color: var(--text-grey);
    margin-top: 4px;
  }
</style>
</head>
<body>
<main class="canvas">
  <section class="business-card">
    <svg class="card-swoosh" viewBox="0 0 1080 617" aria-hidden="true">
      <defs>
        <linearGradient id="purpleBand" x1="0" y1="0" x2="1" y2="1">
          <stop offset="0" stop-color="var(--brand-purple-light)"/>
          <stop offset="0.55" stop-color="var(--brand-purple)"/>
          <stop offset="1" stop-color="var(--brand-purple-deep)"/>
        </linearGradient>
        <linearGradient id="greyBand" x1="0" y1="0" x2="1" y2="1">
          <stop offset="0" stop-color="var(--swoosh-grey-light)"/>
          <stop offset="0.5" stop-color="var(--swoosh-grey)"/>
          <stop offset="1" stop-color="#5d5d60"/>
        </linearGradient>
      </defs>
      <path d="M590,0 C840,40 1020,210 1080,450 L1080,370 C1010,175 870,55 655,0 Z" fill="url(#greyBand)"/>
      <path d="M655,0 L1080,0 L1080,370 C1010,175 870,55 655,0 Z" fill="url(#purpleBand)"/>
      <path d="M700,0 C880,45 1010,160 1080,320" fill="none" stroke="#ffffff" stroke-opacity="0.35" stroke-width="3"/>
    </svg>

    <div class="brand">
      <span class="brand-dot"></span>
      <span class="brand-name">Pinegate Mobile Imaging</span>
    </div>

    <ul class="contact-list">
      <li class="contact-item">
        <svg class="contact-icon" viewBox="0 0 24 24"><circle cx="12" cy="12" r="12" fill="var(--brand-purple)"/><path d="M12 5a4.5 4.5 0 0 0-4.5 4.5C7.5 13 12 19 12 19s4.5-6 4.5-9.5A4.5 4.5 0 0 0 12 5zm0 6.2a1.7 1.7 0 1 1 0-3.4 1.7 1.7 0 0 1 0 3.4z" fill="#fff"/></svg>
        418 Whitford Ave. Ste 203-117
      </li>
      <li class="contact-item continuation">Marrow Falls, KY 40877</li>
      <li class="contact-item">
        <svg class="contact-icon" viewBox="0 0 24 24"><circle cx="12" cy="12" r="12" fill="var(--brand-purple)"/><path d="M8.6 6.2l1.6-.4 1.2 2.8-1.2 1c.6 1.4 1.7 2.5 3.1 3.2l1-1.2 2.8 1.2-.4 1.6c-.2.7-.8 1.1-1.5 1-4-.5-7.1-3.6-7.6-7.6-.1-.7.3-1.4 1-1.6z" fill="#fff"/></svg>
        (270) 555-0148
      </li>
      <li class="contact-item">
        <svg class="contact-icon" viewBox="0 0 24 24"><circle cx="12" cy="12" r="12" fill="var(--brand-purple)"/><circle cx="12" cy="12" r="4" fill="#fff"/></svg>
        Leave space to add later
      </li>
      <li class="contact-item">
        <svg class="contact-icon" viewBox="0 0 24 24"><circle cx="12" cy="12" r="12" fill="var(--brand-purple)"/><rect x="6" y="8" width="12" height="8.5" rx="1" fill="#fff"/><path d="M6.5 8.5l5.5 4.3 5.5-4.3" fill="none" stroke="var(--brand-purple)" stroke-width="1.2"/></svg>
        danelle.forbush@mailbright.net
      </li>
    </ul>

    <div class="owner-block">
      <p class="owner-name">Danelle Forbush &nbsp;RCS, RDCS</p>
      <p class="owner-title">Owner</p>
    </div>
  </section>
</main>
</body>
</html>
```